Medical supplies company needs a catalogue re-design

Our present catalogue is spread over a number of pages but this needs to be reduced. 4-5 images would require to be on each page. It needs to be professional, simple and elegant. The photos and descriptors need to be adjacent to each other. It should be able to be emailed conventionally as an e-catalogue without it being compressed. an email with existing catalogue will be emailed to anyone interested.
https://www.quillvault.net/s/81tazup7rqwmdlon/consumables%20photos%20and%20descriptions.pdf?dl=0
Target Market(s)
medical practices, hospitals
Industry/Entity Type
Medical Supply

```html
<!DOCTYPE html>
<html lang="en">
<head>
<meta charset="utf-8">
<title>Velora Mobility – Winter Catalogue 2018</title>
<link rel="stylesheet" href="https://fonts.googleapis.com/css2?family=Oswald:wght@500;600&family=Arimo:wght@400;700&display=swap">
<style>
:root{
  --red:#e0252f;
  --dark:#1f0a0c;
  --taupe:#8e8281;
  --grey:#a3a3a3;
  --ink:#111;
  --white:#fff;
  --canvas:#e6e6e6;
}
*{box-sizing:border-box;margin:0;padding:0}
html,body{width:1200px;height:1200px;overflow:hidden}
body{background:var(--canvas);font-family:"Arimo",Arial,sans-serif;color:var(--ink);position:relative}
.page{position:absolute;top:118px;width:532px;height:657px;overflow:hidden;box-shadow:0 4px 10px rgba(0,0,0,.25)}
.cover{left:59px;background:var(--white)}
.band{position:absolute;left:0;right:0;background:var(--red)}
.band-top{top:0;height:20px}
.band-bottom{bottom:0;height:24px}
.cover-photo{position:absolute;left:0;top:20px;width:532px;height:355px;
  background:linear-gradient(160deg,#d9b08a 0%,#a66a3e 35%,#7b5a47 60%,#3f4a5e 100%)}
.brand-box{position:absolute;left:7px;top:20px;width:201px;height:90px;background:rgba(255,255,255,.72);border-radius:0 0 8px 8px;padding:20px 0 0 18px}
.brand{font-family:"Oswald",sans-serif;font-weight:600;color:var(--red);font-size:30px;line-height:1;letter-spacing:1px;display:flex;align-items:center;gap:8px}
.brand-dot{width:18px;height:18px;border-radius:50%;background:var(--red)}
.brand-sub{font-family:"Oswald",sans-serif;font-weight:500;font-size:14px;color:var(--ink);margin-top:4px;padding-left:28px}
.year{position:absolute;left:338px;top:251px;width:184px;height:184px;border-radius:50%;background:var(--red);color:var(--white);
  font-family:"Oswald",sans-serif;font-weight:500;font-size:56px;display:flex;align-items:center;justify-content:center}
.cover-title{position:absolute;left:21px;top:440px;font-family:"Oswald",sans-serif;font-weight:600;font-size:54px;line-height:1;transform:scaleX(.92);transform-origin:left;letter-spacing:.5px}
.sections{position:absolute;top:520px;left:12px;display:flex;gap:6px}
.section{height:115px;border-radius:12px;color:var(--white);font-family:"Oswald",sans-serif;font-weight:500;font-size:27px;line-height:1.15;
  display:flex;align-items:center;justify-content:center;text-align:center}
.section-red{width:168px;background:var(--red)}
.section-dark{width:163px;background:var(--dark)}
.section-taupe{width:165px;background:var(--taupe)}

.inner{left:611px;background:var(--grey)}
.inner .band-top{height:25px}
.tab{position:absolute;left:12px;top:0;width:171px;height:41px;background:var(--ink);color:var(--white);border-radius:0 0 10px 10px;
  font-family:"Oswald",sans-serif;font-weight:500;font-size:26px;display:flex;align-items:center;justify-content:center}
.product{position:absolute;left:12px;width:506px;display:flex;gap:7px}
.product-photo{width:171px;height:100%;background:#f1f1f1;border-radius:8px;position:relative;overflow:hidden}
.product-photo span{position:absolute;border-radius:4px}
.product-info{flex:1;background:var(--white);border-radius:8px;padding:3px 8px 0 12px;font-size:8.4px;line-height:1.12}
.product-info h3{font-size:9.4px;font-weight:700;margin-bottom:3px}
.product-info ul{list-style:none}
.product-info li{padding-left:8px;position:relative}
.product-info li::before{content:"•";position:absolute;left:0}
.footer-brand{position:absolute;left:12px;bottom:6px;color:var(--red);font-family:"Oswald",sans-serif;font-weight:500;font-size:20px;line-height:1;display:flex;align-items:center;gap:5px}
.footer-brand small{font-size:9px;color:var(--white);margin-left:2px}
.footer-dot{width:11px;height:11px;border-radius:50%;background:var(--red)}
.footer-brand-wrap{position:absolute;left:12px;bottom:16px}
.page-num{position:absolute;left:448px;bottom:0;width:69px;height:33px;background:var(--ink);color:var(--white);border-radius:10px 10px 0 0;
  font-family:"Oswald",sans-serif;font-weight:500;font-size:22px;display:flex;align-items:center;justify-content:center}
</style>
</head>
<body>

<section class="page cover">
  <div class="band band-top"></div>
  <div class="cover-photo" role="img" aria-label="Photograph of an elderly couple smiling on a swing in front of an autumn house"></div>
  <div class="brand-box">
    <div class="brand">VELORA <span class="brand-dot"></span></div>
    <div class="brand-sub">MOBILITY</div>
  </div>
  <div class="year">2018</div>
  <h1 class="cover-title">WINTER CATALOGUE</h1>
  <div class="sections">
    <div class="section section-red">MEDICAL<br>CONSUMABLE</div>
    <div class="section section-dark">MOBILITY<br>EQUIPMENT</div>
    <div class="section section-taupe">CONSUMER<br>HEALTH</div>
  </div>
  <div class="band band-bottom"></div>
</section>

<section class="page inner">
  <div class="band band-top"></div>
  <div class="tab">WOUND CARE</div>

  <article class="product" style="top:48px;height:66px">
    <div class="product-photo" role="img" aria-label="Red roll of cohesive bandage"></div>
    <div class="product-info">
      <h3>Cohesive Bandages (7.5 cm x 4.5 m, 10cm x 4.5 m)</h3>
      <ul>
        <li>Offers compression to support a joint or muscle</li>
        <li>Secures wound dressings &amp; is painless when removed</li>
        <li>Secures to itself &amp; can be torn by hand</li>
        <li>Won't leave any sticky residue</li>
        <li>Conforms to all body contours</li>
      </ul>
    </div>
  </article>

  <article class="product" style="top:122px;height:66px">
    <div class="product-photo" role="img" aria-label="Box and tins of transparent plaster tape"></div>
    <div class="product-info">
      <h3>Transparent Plaster With Plastic Tin</h3>
      <ul>
        <li>Zinc oxide tape used for securing dresses, particularly along joints and contoured body parts.</li>
        <li>Comfortable and breathable</li>
        <li>Strong adhesion</li>
        <li>2.5cm by 9m (12 per box)</li>
      </ul>
    </div>
  </article>

  <article class="product" style="top:196px;height:107px">
    <div class="product-photo" role="img" aria-label="Packet and pad of non woven adhesive wound dressing"></div>
    <div class="product-info">
      <h3>Non Woven Adhesive Wound Dressing</h3>
      <ul>
        <li>Convenient all in one sterile dressing that can be used for a large range of wound and skin lesions.</li>
        <li>It is well absorbent and non adherent to wounds with minimal risk of skin reactions.</li>
        <li>It protects open wounds and reduces wound infection</li>
        <li>Not waterproof</li>
        <li>Used for both surgical wound care and post traumatic wound closure</li>
        <li>50 pcs per box (6cm by 8cm), 100 pcs per box (10cm by 10cm)</li>
        <li>Sizes: 6cm by 8cm, 10cm by 10cm</li>
      </ul>
    </div>
  </article>

  <article class="product" style="top:312px;height:97px">
    <div class="product-photo" role="img" aria-label="Packet and patch of extra thin hydrocolloid dressing"></div>
    <div class="product-info">
      <h3>Hydrocolloid Dressing (extra thin)</h3>
      <ul>
        <li>This is for low/moderate exudate wounds. Suitable for venous ulcers, bed sores, superficial burns, post operative wounds &amp; healing of chronic ulcers.</li>
        <li>Provides a waterproof barrier over the dressing.</li>
        <li>Does not damage newly formed tissues on removal</li>
        <li>Can be cut to fit</li>
        <li>Needs to be changed every two to three days</li>
        <li>7.5cm by 7.5cm (25pcs per box) &amp; 10cm by 10cm (10 pcs per box)</li>
      </ul>
    </div>
  </article>

  <article class="product" style="top:416px;height:99px">
    <div class="product-photo" role="img" aria-label="Packet and patch of hydrocolloid dressing with thin border"></div>
    <div class="product-info">
      <h3>Hydrocolloid Dressing (with thin border)</h3>
      <ul>
        <li>Used for light to moderate exuding wounds.</li>
        <li>Suitable for venous ulcers, bed sores, superficial burns, post operative wounds and healing of chronic ulcers.</li>
        <li>Contains hydrocolloid dressing with thin border which facilitates the adherence of the hydrocolloid dressing to the wound</li>
        <li>On removal, does not damage the newly formed healing tissue.</li>
        <li>Change of dressing every two to three days</li>
        <li>7.5cm by 7.5cm (25pcs per box) and 10cm by 10cm (10pcs per box)</li>
      </ul>
    </div>
  </article>

  <article class="product" style="top:523px;height:96px">
    <div class="product-photo" role="img" aria-label="Packet and pad of self adhesive silicone foam dressing"></div>
    <div class="product-info">
      <h3>Silicone Foam Dressing (Self Adhesive)</h3>
      <ul>
        <li>Suitable for low to high exudative wounds. Can be used for all stages of wound healing</li>
        <li>Can be used for 1) First to third degree burns 2) Skin graft donor and recipient sites 3) Ulcers, pressure sores and cavity wounds 4) Post surgical wounds 4) Infected wounds with copious exudate</li>
        <li>The foam dressing absorbs excess exudate and offers a waterproof bacteria resistant environment.</li>
        <li>10cm by 10cm (10 pcs per box)</li>
      </ul>
    </div>
  </article>

  <div class="band band-bottom"></div>
  <div class="footer-brand-wrap">
    <div class="footer-brand">VELORA <span class="footer-dot"></span></div>
  </div>
  <div class="footer-brand" style="bottom:3px;left:28px;font-size:9px;color:var(--white)">MOBILITY</div>
  <div class="page-num">2</div>
</section>

</body>
</html>
```